Flyer für Alltagsbegleitung
Zielgruppe
Firma: Tageshilfe am Fluss
Meine Zielgruppe sind alle Menschen, die im Alltag, Hilfe benötigen.
Aufgabenstellung
Der Flyer soll modern und und ansprechend aussehen. Es soll vermerkt sein, das ich als annerkannte Kraft, Entlastungsleistung nach

```html
<!DOCTYPE html>
<html lang="de">
<head>
<meta charset="utf-8">
<title>Tageshilfe am Fluss – Flyer</title>
<link href="https://fonts.googleapis.com/css2?family=Baloo+2:wght@600;800&family=Delius&display=swap" rel="stylesheet">
<style>
  :root{
    --page:#e9e8e4;
    --paper:#f7f8f9;
    --slate:#4a6382;
    --sky:#cfdbe8;
    --apricot:#f5bd84;
    --ink:#4a6382;
    --photo-a:#9fb3c6;
    --photo-b:#d9c7b5;
  }
  *{box-sizing:border-box;margin:0;padding:0}
  html,body{width:1200px;height:885px;overflow:hidden;background:var(--page)}
  body{position:relative;font-family:"Delius",cursive}
  .sheet{position:absolute;width:1120px;height:792px;background:var(--paper);display:flex;box-shadow:0 3px 14px rgba(0,0,0,.14);transform:scale(.5223);transform-origin:0 0}
  .sheet-outside{left:14px;top:458px}
  .sheet-inside{left:600px;top:18px}
  .panel{position:relative;width:373.33px;height:100%;overflow:hidden}
  .heading{font-family:"Baloo 2",sans-serif;font-weight:800;text-transform:uppercase;letter-spacing:.02em}
  .brand{position:absolute;display:flex;align-items:center;gap:7px;font-size:14px;color:var(--ink)}
  .brand-dot{width:14px;height:14px;border-radius:50%;background:var(--slate)}

  /* Outside: cover */
  .cover .brand{left:24px;top:30px}
  .cover-band{position:absolute;left:14px;top:200px;width:316px;height:592px;background:var(--slate);border-radius:22px 22px 0 0}
  .cover-photo{position:absolute;left:26px;top:80px;width:290px;height:400px;border-radius:20px;background:linear-gradient(135deg,var(--photo-a),var(--photo-b))}
  .cover-title{position:absolute;left:34px;top:512px;color:#fff;font-size:27px;line-height:1}
  .cover-sub{position:absolute;left:34px;top:548px;color:#fff;font-size:21px;line-height:1.2}
  .cover-icon{position:absolute;left:220px;top:636px}
  .cover-url{position:absolute;left:34px;top:742px;color:#fff;font-family:"Baloo 2",sans-serif;font-weight:800;font-size:12px;text-transform:uppercase}

  /* Outside: about */
  .about{background:var(--sky)}
  .quote{position:absolute;left:34px;top:60px;width:310px;color:var(--ink);font-size:21px;line-height:1.2}
  .quote-author{position:absolute;left:34px;top:186px;font-size:13px;color:var(--ink)}
  .about-title{position:absolute;left:50px;top:262px;color:var(--ink);font-size:20px}
  .about-text{position:absolute;left:50px;top:300px;width:270px;color:var(--ink);font-size:14.5px;line-height:1.5}
  .portrait{position:absolute;left:196px;top:478px;width:110px;height:160px;border-radius:14px;background:linear-gradient(160deg,#e8d7c4,#c9a98a)}
  .cta{position:absolute;left:86px;top:660px;width:250px;height:40px;border-radius:20px;background:#fff;display:flex;align-items:center;justify-content:center;color:var(--ink);font-size:11.5px}

  /* Outside: contact */
  .contact-photo{position:absolute;left:0;top:0;width:373px;height:430px;background:linear-gradient(160deg,#a7c08f,#c7cfd6 55%,#b6a7c9)}
  .contact-tab{position:absolute;left:34px;top:412px;width:110px;height:40px;background:var(--slate);border-radius:12px 12px 0 0;color:#fff;font-size:15px;display:flex;align-items:center;justify-content:center}
  .contact-card{position:absolute;left:22px;top:450px;width:351px;height:248px;background:var(--apricot);border-radius:18px 0 0 18px;padding:30px 24px;color:var(--ink)}
  .contact-name{font-size:18px}
  .contact-line{font-size:14px;line-height:1.5}
  .contact-mail{font-family:"Baloo 2",sans-serif;font-weight:800;font-size:12px;text-transform:uppercase}
  .contact-company{margin-top:28px;font-size:18px}
  .contact-url{margin-top:14px;font-family:"Baloo 2",sans-serif;font-weight:800;font-size:12px;text-transform:uppercase}
  .contact-icon{position:absolute;right:26px;top:112px}

  /* Inside: philosophy */
  .philosophy{background:var(--sky)}
  .philosophy-title{position:absolute;left:54px;top:58px;color:var(--ink);font-size:22px;line-height:1.1}
  .philosophy-text{position:absolute;left:54px;top:122px;width:280px;color:var(--ink);font-size:15px;line-height:1.55}

  /* Inside: services */
  .services-title{position:absolute;left:26px;top:92px;color:var(--ink);font-size:19px}
  .service{position:absolute;border-radius:18px;padding:18px 20px;color:#fff}
  .service-title{font-size:15px;line-height:1.15;margin-bottom:8px}
  .service-list{list-style:none;font-size:12.5px;line-height:1.45}
  .service-list li::before{content:"• "}
  .service-photo{position:absolute;border-radius:20px}
  .service-1-photo{left:26px;top:140px;width:170px;height:150px;background:linear-gradient(140deg,#c9d8b8,#b7a9b8)}
  .service-1{left:170px;top:158px;width:190px;height:150px;background:var(--slate)}
  .service-2-photo{left:170px;top:328px;width:180px;height:150px;background:linear-gradient(140deg,#e7d9cf,#c9b3a4)}
  .service-2{left:20px;top:318px;width:190px;height:156px;background:var(--slate)}
  .service-3{left:50px;top:500px;width:260px;height:150px;background:var(--sky);color:var(--ink)}
  .services-note{position:absolute;left:26px;top:676px;width:320px;color:var(--ink);font-size:13px}

  /* Inside: recognition */
  .recognition .brand{right:30px;top:30px}
  .recognition-card{position:absolute;left:22px;top:84px;width:326px;height:300px;background:var(--apricot);border-radius:22px;padding:34px 30px;color:var(--ink)}
  .recognition-title{color:#fff;font-size:28px;line-height:1.1;margin-bottom:22px}
  .recognition-text{font-size:15px;line-height:1.5}
  .recognition-photo{position:absolute;left:22px;top:404px;width:326px;height:330px;border-radius:22px;background:linear-gradient(150deg,#f1eef3,#d9cfe4 60%,#c9a08f)}
</style>
</head>
<body>

<main class="sheet sheet-inside">
  <section class="panel philosophy">
    <h2 class="heading philosophy-title">Unsere<br>Philosophie</h2>
    <p class="philosophy-text">Miteinander. Alltag. Leichter. Jeder Mensch verdient ein Leben in Würde – auch (und besonders) im Alltag. Mit meiner Arbeit möchte ich dazu beitragen, dass Menschen mit Unterstützungsbedarf möglichst selbstbestimmt bleiben können – mit Herz, Respekt und Verlässlichkeit. Ich sehe meine Aufgabe nicht nur im Helfen, sondern vor allem im Zuhören, Verstehen und Begleiten. Denn oft ist es die kleine Entlastung, die einen großen Unterschied macht – für Pflegebedürftige ebenso wie für Angehörige.</p>
  </section>

  <section class="panel services">
    <h2 class="heading services-title">Leistungen</h2>
    <div class="service-photo service-1-photo" role="img" aria-label="Foto: Helferin unterstützt eine ältere Dame zu Hause"></div>
    <div class="service service-1">
      <h3 class="heading service-title">Hilfe im Alltag &amp; Haushalt</h3>
      <ul class="service-list"><li>Jeden Freitag</li><li>12:00 bis 13:00 Uhr</li><li>20€/Stunde</li><li>Mit Anmeldung</li></ul>
    </div>
    <div class="service-photo service-2-photo" role="img" aria-label="Foto: Hände halten einander zur Begleitung"></div>
    <div class="service service-2">
      <h3 class="heading service-title">Begleitung bei Arztbesuchen oder Einkäufen</h3>
      <ul class="service-list"><li>Nach Absprache</li><li>20€/Stunde</li><li>Mit Anmeldung</li></ul>
    </div>
    <div class="service service-3">
      <h3 class="heading service-title">Gespräche, Gesellschaft, Spaziergänge</h3>
      <ul class="service-list"><li>15:00 bis 16:00 Uhr</li><li>20€/Stunde</li><li>Mit Anmeldung</li></ul>
    </div>
    <p class="heading services-note">Über die Pflegekasse abrechenbar!</p>
  </section>

  <section class="panel recognition">
    <div class="brand"><span class="brand-dot"></span>Lena Hofmann</div>
    <div class="recognition-card">
      <h2 class="heading recognition-title">Anerkannte<br>Betreuung</h2>
      <p class="recognition-text">Als anerkannte Betreuungskraft nach § 45b SGB XI bin ich berechtigt, meine Leistungen mit der Pflegekasse abzurechnen. Sprechen Sie mich gerne an – ich erkläre Ihnen alles Schritt für Schritt.</p>
    </div>
    <div class="recognition-photo" role="img" aria-label="Foto: Hände halten ein rotes Herz"></div>
  </section>
</main>

<main class="sheet sheet-outside">
  <section class="panel cover">
    <div class="brand"><span class="brand-dot"></span>Lena Hofmann</div>
    <div class="cover-band"></div>
    <div class="cover-photo" role="img" aria-label="Foto: Pflegekraft im Gespräch mit einem älteren Herrn"></div>
    <h1 class="heading cover-title">Alltagsbegleitung</h1>
    <p class="cover-sub">Mit Herz, Verlässlichkeit<br>&amp; Erfahrung</p>
    <svg class="cover-icon" width="70" height="60" viewBox="0 0 70 60" fill="none" stroke="#fff" stroke-width="1.6" stroke-linecap="round" stroke-linejoin="round">
      <path d="M35 30 C22 20 24 8 32 10 C34 10.5 35 12 35 14 C35 12 36 10.5 38 10 C46 8 48 20 35 30Z"/>
      <path d="M6 44 C16 40 24 40 32 44 L46 44 C50 44 50 50 46 50 L34 50"/>
      <path d="M44 48 L58 40 C62 38 65 42 62 45 L46 56 C40 59 24 58 6 54"/>
    </svg>
    <p class="cover-url">www.tageshilfe-fluss.de</p>
  </section>

  <section class="panel about">
    <p class="heading quote">„Sich um diejenigen zu kümmern, die sich einst um uns gekümmert haben, ist eine der grössten Ehren.“</p>
    <p class="quote-author">– M. Berger</p>
    <h2 class="heading about-title">Wer bin ich?</h2>
    <p class="about-text">Mein Name ist Lena Hofmann. Als anerkannte Betreuungskraft nach § 45b SGB XI unterstütze ich Menschen mit Pflegegrad im Alltag – flexibel, menschlich und individuell. Ich biete Hilfe im Haushalt, Begleitung zu Terminen oder einfach nur ein offenes Ohr – ganz nach Ihren Bedürfnissen.</p>
    <div class="portrait" role="img" aria-label="Porträtfoto der Betreuungskraft"></div>
    <div class="heading cta">Erfahre mehr auf unserer Website</div>
  </section>

  <section class="panel contact">
    <div class="contact-photo" role="img" aria-label="Foto: Pflegerin begleitet eine ältere Dame mit Rollator im Grünen"></div>
    <div class="heading contact-tab">Kontakt</div>
    <div class="contact-card">
      <p class="contact-name">Lena Hofmann</p>
      <p class="contact-line">Phone: 01520 448317</p>
      <p class="contact-mail">E-Mail: olup.hofmann@email.com</p>
      <p class="contact-company">Tageshilfe am Fluss</p>
      <p class="contact-line">Uferweg 12, 12345, Musterstadt</p>
      <p class="contact-url">www.tageshilfe-fluss.de</p>
      <svg class="contact-icon" width="46" height="46" viewBox="0 0 46 46" fill="none" stroke="#4a6382" stroke-width="1.6" stroke-linecap="round" stroke-linejoin="round">
        <circle cx="17" cy="10" r="6"/>
        <path d="M6 32 C6 22 28 22 28 32"/>
        <path d="M34 30 C27 25 28 18 32 19 C33 19.3 34 20 34 21 C34 20 35 19.3 36 19 C40 18 41 25 34 30Z"/>
        <path d="M4 40 L24 40 L34 34"/>
      </svg>
    </div>
  </section>
</main>

</body>
</html>
```